La etiqueta deberá contener lo siguiente:
-Titulo: Miel de Agave Kosher
-Logo de DOVRA (realizado por ustedes, adjunto diseño)
-Logo del certificado: KOSHER (Se adjuntan certificado)
-Mililitros: 750 ml
-Información nutrimental: se adjunta tabla
La miel deberá sobresalir de las demás por el estilo lujoso y llamativo de la etiqueta.

```html
<!DOCTYPE html>
<html lang="es">
<head>
<meta charset="utf-8">
<title>DOVRA · Miel de Agave Kosher</title>
<link href="https://fonts.googleapis.com/css2?family=Jost:wght@400;600&display=swap" rel="stylesheet">
<style>
  :root{
    --paper:#ffffff;
    --ink:#000000;
    --gold-dark:#c8901c;
    --gold-light:#f3dc3e;
    --gold-mid:#e0b52a;
    --pattern-a:#1c1c1c;
    --pattern-b:#0b0b0b;
    --muted:#5a5a5a;
    --muted-soft:#4a4a4a;
  }
  html,body{margin:0;padding:0;overflow:hidden;background:var(--paper);}
  .canvas{position:relative;width:1200px;height:1200px;background:var(--paper);overflow:hidden;font-family:"Jost",sans-serif;}
  .label-art{position:absolute;left:0;top:0;width:1200px;height:1200px;}
  .brand{position:absolute;left:0;width:1200px;top:508px;text-align:center;color:var(--gold-mid);font-weight:400;font-size:26px;letter-spacing:6px;}
  .brand-dot{position:absolute;left:589px;top:446px;width:22px;height:22px;border-radius:50%;background:var(--gold-mid);}
  .title{position:absolute;left:0;width:1200px;top:580px;text-align:center;color:var(--gold-mid);font-weight:600;font-size:31px;letter-spacing:6px;line-height:36px;}
  .volume{position:absolute;left:0;width:1200px;top:758px;text-align:center;color:var(--muted);font-size:13px;}
  .importer{position:absolute;left:150px;top:740px;color:var(--muted-soft);font-size:8.5px;line-height:11px;}
  .importer span{text-decoration:underline;}
  .nutrition{position:absolute;left:914px;top:591px;width:133px;height:168px;border:1px solid var(--muted-soft);color:var(--muted);font-family:Arial,sans-serif;font-size:5.2px;line-height:7.6px;box-sizing:border-box;padding:3px 4px;}
  .nutrition h2{margin:0 0 8px;font-size:13.5px;line-height:13px;text-align:center;color:var(--muted);font-weight:700;}
  .nutrition .row{display:flex;justify-content:space-between;}
  .nutrition .row.indent span:first-child{padding-left:14px;}
  .nutrition .rule{border-top:1.5px solid var(--muted);margin:2px 0;}
  .nutrition strong{font-weight:700;}
</style>
</head>
<body>
<div class="canvas">
  <svg class="label-art" viewBox="0 0 1200 1200" xmlns="http://www.w3.org/2000/svg">
    <defs>
      <linearGradient id="gold" x1="0" x2="1" y1="0" y2="0">
        <stop offset="0" stop-color="#c8901c"/>
        <stop offset="0.5" stop-color="#f3dc3e"/>
        <stop offset="1" stop-color="#c8901c"/>
      </linearGradient>
      <radialGradient id="pattern" cx="0.5" cy="0.5" r="0.7">
        <stop offset="0" stop-color="#1c1c1c"/>
        <stop offset="1" stop-color="#0b0b0b"/>
      </radialGradient>
      <radialGradient id="comb" cx="0.5" cy="0.5" r="0.6">
        <stop offset="0" stop-color="#141414"/>
        <stop offset="1" stop-color="#050505"/>
      </radialGradient>
    </defs>
    <rect class="band-top" x="139" y="429" width="926" height="11" fill="url(#gold)"/>
    <rect class="band-bottom" x="139" y="769" width="926" height="11" fill="url(#gold)"/>
    <rect class="band-body" x="139" y="440" width="926" height="329" fill="url(#pattern)" role="img" aria-label="Patrón decorativo de trazos curvos grises sobre negro"/>
    <polygon class="hex-outer" points="494,420 709,420 816,605 709,790 494,790 389,605" fill="url(#gold)"/>
    <polygon class="hex-gap" points="498,426 705,426 809,605 705,784 498,784 396,605" fill="var(--ink)"/>
    <polygon class="hex-line" points="502,432 701,432 802,605 701,778 502,778 402,605" fill="url(#gold)"/>
    <polygon class="hex-core" points="504,435 699,435 799,605 699,775 504,775 405,605" fill="url(#comb)" role="img" aria-label="Textura de panal de abeja en negro"/>
    <circle class="seal" cx="602" cy="712" r="44" fill="url(#gold)"/>
    <circle cx="602" cy="712" r="36" fill="var(--ink)"/>
    <circle cx="602" cy="712" r="30" fill="url(#gold)"/>
  </svg>

  <div class="brand-dot"></div>
  <div class="brand">DOVRA</div>
  <div class="title">MIEL DE AGAVE<br>KOSHER</div>
  <div class="volume">750ml</div>

  <div class="importer"><span>Importada por</span><br>www.dovra-miel.mx</div>

  <div class="nutrition">
    <h2>Declaración Nutrimental</h2>
    <div class="row"><strong>Contenido energético por envase</strong><span>2,050 kcal</span></div>
    <div class="row"><span></span><span>8,639 kJ</span></div>
    <div class="rule"></div>
    <div class="row"><span>Tamaño de la porción</span><span>100g</span></div>
    <div class="row"><span>Porciones por envase</span><span>3.3</span></div>
    <div class="row"><span>Contenido energético por porción</span><span>310 kcal</span></div>
    <div class="row"><span></span><span>1,309 kJ</span></div>
    <div class="rule"></div>
    <div class="row"><span>Proteínas</span><span>0 g</span></div>
    <div class="row"><span>Grasas</span><span>0 g</span></div>
    <div class="row indent"><span>Grasa saturada</span><span>0 g</span></div>
    <div class="row indent"><span>Grasas trans</span><span>0 mg</span></div>
    <div class="row"><span>Hidratos de carbono disponibles</span><span>77 g</span></div>
    <div class="row indent"><span>Azúcares</span><span>77 g</span></div>
    <div class="row indent"><span>Azúcares añadidos</span><span>0 g</span></div>
    <div class="row"><span>Fibra dietética</span><span>menos de 1 g</span></div>
    <div class="row"><span>Sodio</span><span>0 mg</span></div>
  </div>
</div>
</body>
</html>
```